New Fun, Positive, energised looking Business Card Needed for High Achiever Coach

I am looking for a two sided full colour business card. I am self employed and have recently re branded my 1-2-1 work re-vitalising high achievers. My target client base for these cards is therefore high achievers - usually aged 40 -55, they are often entrepreneurs, CEO or work in banking and finance and 2/3 are male. I work with them on 90 day or 6 month coaching programs to help them live their success in a healthier, more sustainable and fulfiiled way. They pay for this privately so though they are corporate types the cards need not look 'corporate'. I want to portray the idea of transformation, vitality and re-connecting.
You can get a feel for the look I like on my new website: corinvale.co.uk
I want to use this logo with strapline (Re-Vitalising High Achievers) (I purchased off Logoharbor) and font/ colours (the turquoise and green).
Details to include on the card:
www.corinvale.co.uk
+44 7915 264318
mira@corinvale.co.uk
skype: miracorin
I'd also like to include:
Do you struggle to switch off? Want to be healthier and feel fitter? Want closer relationships? More clarity over the direction you are headed? I can help you do these things using integrated mind-body techniques. Visit corinvale.co.uk TODAY to apply for a FREE Breakthrough session.
BUT if that is too much text for a card I am open to advice/ammendments.
Updates
Thanks for your design - I am considering them. PLease change the wording to :

```html
<!DOCTYPE html>
<html lang="en">
<head>
<meta charset="utf-8">
<title>Mira Corin – Business Card</title>
<link rel="stylesheet" href="https://fonts.googleapis.com/css2?family=Merriweather:ital,wght@0,400;0,700;0,900;1,400&display=swap">
<style>
  :root {
    --stage: #2e2e2e;
    --paper: #ffffff;
    --paper-shade: #ececec;
    --teal: #1a8cab;
    --teal-deep: #0f7f9f;
    --teal-light: #12a3c6;
    --green: #5aab4b;
    --ink-light: #f3fbff;
  }
  * { box-sizing: border-box; margin: 0; padding: 0; }
  html, body {
    width: 1200px; height: 900px; overflow: hidden;
    background: var(--stage);
    font-family: "Merriweather", Georgia, serif;
  }
  .stage {
    position: relative; width: 1200px; height: 900px;
    display: flex; justify-content: center; align-items: center; gap: 70px;
  }
  .card {
    position: relative; width: 380px; height: 620px;
    border-radius: 24px; overflow: hidden;
    background: linear-gradient(180deg, var(--paper) 0%, var(--paper) 60%, var(--paper-shade) 100%);
    box-shadow: 0 18px 40px rgba(0,0,0,.45);
  }
  .brand {
    position: absolute; left: 0; right: 0; top: 56px;
    text-align: center;
  }
  .brand-dot {
    width: 70px; height: 70px; border-radius: 50%;
    background: var(--green); margin: 0 auto 24px;
  }
  .brand-name {
    font-weight: 900; font-size: 40px; color: var(--teal);
    letter-spacing: .5px; line-height: 1;
  }
  .brand-tagline {
    margin-top: 10px; font-size: 15px; color: var(--teal);
    font-style: italic; font-weight: 400;
  }
  /* front */
  .front .dome { position: absolute; left: 0; top: 0; width: 380px; height: 620px; }
  .front .pitch {
    position: absolute; left: 40px; right: 40px; top: 332px;
    text-align: center; color: var(--ink-light);
    font-size: 13.5px; line-height: 1.5;
  }
  .pitch p + p {
    margin: 12px 30px 0; padding-top: 12px;
    border-top: 1.5px dotted rgba(255,255,255,.7);
  }
  .pitch p + p { margin-left: 30px; margin-right: 30px; }
  .pitch strong { font-weight: 700; }
  /* back */
  .back .contacts {
    position: absolute; left: 40px; right: 40px; top: 262px;
    list-style: none; text-align: center;
  }
  .contact-item { padding: 10px 0 6px; }
  .contact-item + .contact-item { border-top: 1.5px dotted var(--teal); }
  .contact-label {
    display: block; color: var(--green); font-weight: 700;
    font-size: 13px; letter-spacing: 1px;
  }
  .contact-value {
    display: block; color: var(--teal); font-size: 20px; margin-top: 4px;
  }
  .back .base-band {
    position: absolute; left: 0; right: 0; bottom: 0; height: 26px;
    background: var(--green);
  }
</style>
</head>
<body>
<main class="stage">

  <section class="card front" aria-label="Card front">
    <svg class="dome" viewBox="0 0 380 620" aria-hidden="true">
      <defs>
        <linearGradient id="domeFill" x1="0" y1="0" x2="0" y2="1">
          <stop offset="0" stop-color="#12a3c6"/>
          <stop offset="1" stop-color="#0f7f9f"/>
        </linearGradient>
      </defs>
      <path d="M0,390 A214.5,214.5 0 0 1 380,390 L380,620 L0,620 Z" fill="url(#domeFill)"/>
      <path d="M0,390 A214.5,214.5 0 0 1 380,390" fill="none" stroke="#5aab4b" stroke-width="4"/>
    </svg>
    <div class="brand">
      <div class="brand-dot"></div>
      <div class="brand-name">Mira Corin</div>
      <div class="brand-tagline">Re-Vitalising High Achievers</div>
    </div>
    <div class="pitch">
      <p>Do you struggle to switch off?<br>Want to be healthier and feel fitter?<br>Want closer relationships?<br>More clarity over the direction you<br>are headed?</p>
      <p>Let me help you reach your goals<br>using integrated mind-body techniques.</p>
      <p>Visit <strong>corinvale.co.uk</strong> TODAY<br>to apply for a FREE Breakthrough<br>session.</p>
    </div>
  </section>

  <section class="card back" aria-label="Card back">
    <div class="brand">
      <div class="brand-dot"></div>
      <div class="brand-name">Mira Corin</div>
      <div class="brand-tagline">Re-Vitalising High Achievers</div>
    </div>
    <ul class="contacts">
      <li class="contact-item"><span class="contact-label">PHONE</span><span class="contact-value">+44 7915 264318</span></li>
      <li class="contact-item"><span class="contact-label">EMAIL</span><span class="contact-value">mira@corinvale.co.uk</span></li>
      <li class="contact-item"><span class="contact-label">SKYPE</span><span class="contact-value">miracorin</span></li>
      <li class="contact-item"><span class="contact-label">WEB</span><span class="contact-value">www.corinvale.co.uk</span></li>
    </ul>
    <div class="base-band"></div>
  </section>

</main>
</body>
</html>
```